Culture consulting company business card - first step

I created a new venture called The Harbor Keystone. It's focused on improving the organizational culture of companies and I have a logo, tag line and other basic info but I need an overall design theme I'll carry through to letterhead, marketing literature, direct mail post cards, whitepapers, video intros and my web site. The business card design is a trial to develop the theme and more projects will hopefully follow for the winner! This business will grow fast and I need a great design theme to leverage.

Target Market(s)

Target Market is both for profit and non profit businesses. Special emphasis on consulting companies, foundations and venture capital firms

Industry/Entity Type

Marketing

Requirements
Must have
• The Harbor Keystone Logo
Name (Ned Wastrom)
Phone (313-574-6190)
E-mail (Ned@The-Harbor-Keystone.com)
Web Site (www.The-Harbor-Keystone.com)
Tag line in some way: "Culture Change with Clarity and Speed"
- Clarity and Speed should be in red with speed potentially in italics. The other words in black.

Front and back of card design - front has info above
Back should have The Harbor Keystone logo and a list of areas we focus on with the red check mark image next to each. The areas are: Performance Improvement, Organizational Excellence, Strategic Alignment, Team Effectiveness, Onboarding, Leadership Development & Coaching

Overall key colors are in the logo (red & black)

NEED DESIGN FORMAT in a PHOTOSHOP / PSD FILE. Photoshop template from printer is attached. Needs to follow the diminsions / guidelines.
Nice to have
• Potentially "road" picture if it fits with a great theme
Should not have
• Needs to be veryprofessional looking but it's fine to come across as very innovative, interesting or unique. Need clear design / fonts and color theme I can carry through to other print and web formats.

```html
<!DOCTYPE html>
<html lang="en">
<head>
<meta charset="utf-8">
<title>The Harbor Keystone – Business Card</title>
<link rel="stylesheet" href="https://fonts.googleapis.com/css2?family=Arimo:wght@400;700&display=swap">
<style>
  :root {
    --stage: #3c3c3c;
    --ink: #111111;
    --red: #e31b2d;
    --paper: #ececec;
    --white: #ffffff;
    --road-light: #d4d4d2;
    --road-dark: #8e8e8c;
  }
  * { margin: 0; padding: 0; box-sizing: border-box; }
  html, body { width: 1200px; height: 534px; overflow: hidden; }
  body {
    background: var(--stage);
    font-family: "Arimo", Arial, sans-serif;
    position: relative;
  }
  .card {
    position: absolute;
    top: 125px;
    width: 525px;
    height: 286px;
    overflow: hidden;
  }
  .card svg.card-art { position: absolute; inset: 0; }
  .card--back { left: 59px; background: var(--ink); }
  .card--front { left: 617px; background: var(--paper); }

  .brand-name {
    position: absolute;
    font-weight: 700;
    color: var(--ink);
    text-transform: uppercase;
    text-align: center;
    line-height: 1.05;
  }
  .card--back .brand-name {
    left: 20px; top: 148px; width: 170px;
    font-size: 22px;
  }
  .card--front .brand-name {
    left: 28px; top: 82px; width: 190px;
    font-size: 23px;
  }

  .focus-list {
    position: absolute;
    left: 266px; top: 69px;
    list-style: none;
  }
  .focus-list li {
    color: var(--white);
    font-size: 13.5px;
    height: 22px;
    display: flex;
    align-items: center;
  }
  .focus-list .tick { width: 11px; height: 11px; margin-right: 6px; }

  .web-link {
    position: absolute;
    left: 247px; top: 243px;
    color: var(--red);
    font-size: 14px;
  }

  .divider {
    position: absolute;
    left: 250px; top: 80px;
    width: 1px; height: 88px;
    background: #555;
  }
  .contact { position: absolute; left: 270px; top: 78px; }
  .contact-name {
    color: var(--red);
    font-size: 17px;
    font-weight: 700;
    margin-bottom: 9px;
  }
  .contact-line {
    font-size: 13px;
    color: var(--ink);
    height: 22px;
  }
  .contact-line .label { color: var(--red); }

  .tagline {
    position: absolute;
    left: 0; right: 0; top: 260px;
    text-align: center;
    color: var(--white);
    font-size: 14.5px;
    font-weight: 700;
  }
  .tagline .accent { color: var(--red); }
</style>
</head>
<body>

  <section class="card card--back">
    <svg class="card-art" viewBox="0 0 525 286" width="525" height="286" aria-hidden="true">
      <defs>
        <linearGradient id="roadTone" x1="0" y1="0" x2="0.6" y2="1">
          <stop offset="0" stop-color="var(--road-light)"/>
          <stop offset="0.45" stop-color="#b8b8b6"/>
          <stop offset="1" stop-color="var(--road-dark)"/>
        </linearGradient>
      </defs>
      <path d="M0,0 L182,0 C228,40 230,130 222,175 C214,225 208,262 222,286 L0,286 Z" fill="var(--red)"/>
      <path d="M0,0 L176,0 C214,40 216,130 208,175 C200,225 194,262 206,286 L0,286 Z" fill="var(--white)"/>
      <path d="M0,0 L170,0 C206,40 208,130 200,175 C192,225 186,262 196,286 L0,286 Z" fill="url(#roadTone)" role="img" aria-label="Photograph of a curving open highway"/>
    </svg>
    <div class="brand-name">The<br>Harbor<br>Keystone</div>
    <ul class="focus-list">
      <li><svg class="tick" viewBox="0 0 12 12"><path d="M1,6 L4.5,11 L11,0.5 L4.5,8 Z" fill="var(--red)"/></svg>Performance Improvement</li>
      <li><svg class="tick" viewBox="0 0 12 12"><path d="M1,6 L4.5,11 L11,0.5 L4.5,8 Z" fill="var(--red)"/></svg>Strategic Alignment</li>
      <li><svg class="tick" viewBox="0 0 12 12"><path d="M1,6 L4.5,11 L11,0.5 L4.5,8 Z" fill="var(--red)"/></svg>Team Effectiveness</li>
      <li><svg class="tick" viewBox="0 0 12 12"><path d="M1,6 L4.5,11 L11,0.5 L4.5,8 Z" fill="var(--red)"/></svg>Employee Engagement</li>
      <li><svg class="tick" viewBox="0 0 12 12"><path d="M1,6 L4.5,11 L11,0.5 L4.5,8 Z" fill="var(--red)"/></svg>Mergers &amp; Acquisitions</li>
      <li><svg class="tick" viewBox="0 0 12 12"><path d="M1,6 L4.5,11 L11,0.5 L4.5,8 Z" fill="var(--red)"/></svg>Executive Onboarding</li>
      <li><svg class="tick" viewBox="0 0 12 12"><path d="M1,6 L4.5,11 L11,0.5 L4.5,8 Z" fill="var(--red)"/></svg>Culture &amp; Leadership Coaching</li>
    </ul>
    <div class="web-link">www.The-Harbor-Keystone.com</div>
  </section>

  <section class="card card--front">
    <svg class="card-art" viewBox="0 0 525 286" width="525" height="286" aria-hidden="true">
      <path d="M0,228 C110,215 220,240 340,222 C430,208 490,196 525,182 L525,286 L0,286 Z" fill="var(--red)"/>
      <path d="M0,240 C110,226 220,250 340,232 C430,218 490,210 525,202 L525,286 L0,286 Z" fill="var(--white)"/>
      <path d="M0,246 C110,232 220,255 340,238 C430,225 490,216 525,210 L525,286 L0,286 Z" fill="var(--ink)"/>
    </svg>
    <div class="brand-name">The<br>Harbor<br>Keystone</div>
    <div class="divider"></div>
    <div class="contact">
      <div class="contact-name">Ned Wastrom</div>
      <div class="contact-line"><span class="label">p:</span> 313.574.6190</div>
      <div class="contact-line"><span class="label">e:</span> Ned@The-Harbor-Keystone.com</div>
      <div class="contact-line"><span class="label">w:</span> www.The-Harbor-Keystone.com</div>
    </div>
    <div class="tagline"><span class="accent">Breakthrough</span> Results with <span class="accent">Clarity</span> and <span class="accent">Speed</span></div>
  </section>

</body>
</html>
```